Im open to ideas.. I was thinking on my business cards aswell as my logo. a place for my name. email. phone number and abn..

ive attched a file with my business logo. which i dont love the colours.. i was think a dark background with charcoal letters so something along those colour schumes but im open to ideas..

Business

BRL Constructions

```html
<!DOCTYPE html>
<html lang="en">
<head>
<meta charset="utf-8">
<title>BRL Constructions – Business Card</title>
<link href="https://fonts.googleapis.com/css2?family=Oswald:wght@500;600&family=Open+Sans:wght@400&display=swap" rel="stylesheet">
<style>
  :root {
    --page-bg: #e9e7e4;
    --card-bg: #ffffff;
    --frame: #d6d6d6;
    --charcoal: #231f20;
    --accent-red: #e5232b;
    --text-grey: #3a3a3a;
    --divider: #cfcfcf;
  }
  html, body {
    margin: 0;
    width: 1200px;
    height: 1000px;
    overflow: hidden;
    background: var(--page-bg);
  }
  .canvas {
    width: 1200px;
    height: 1000px;
    display: flex;
    align-items: center;
    justify-content: center;
  }
  .business-card {
    position: relative;
    width: 1000px;
    height: 572px;
    background: var(--card-bg);
    box-shadow: 0 2px 10px rgba(0,0,0,0.12);
  }
  .card-frame {
    position: absolute;
    inset: 18px;
    border: 2px solid var(--frame);
  }
  .brand-name {
    position: absolute;
    top: 140px;
    left: 0;
    right: 0;
    text-align: center;
    font-family: "Oswald", sans-serif;
    font-weight: 600;
    font-size: 84px;
    letter-spacing: 4px;
    line-height: 1;
    color: var(--charcoal);
    text-transform: uppercase;
  }
  .person {
    position: absolute;
    top: 330px;
    right: 530px;
    text-align: right;
  }
  .person-name {
    font-family: "Oswald", sans-serif;
    font-weight: 500;
    font-size: 25px;
    color: var(--accent-red);
    text-transform: uppercase;
    letter-spacing: 0.5px;
    line-height: 1.2;
  }
  .person-title {
    font-family: "Open Sans", sans-serif;
    font-size: 20px;
    color: var(--text-grey);
    margin-top: 2px;
  }
  .section-divider {
    position: absolute;
    left: 492px;
    top: 300px;
  }
  .contact-list {
    position: absolute;
    top: 300px;
    left: 540px;
    margin: 0;
    padding: 0;
    list-style: none;
    font-family: "Open Sans", sans-serif;
    font-size: 20px;
    color: var(--text-grey);
  }
  .contact-item {
    display: flex;
    align-items: center;
    gap: 10px;
    height: 30px;
  }
  .contact-icon {
    width: 16px;
    height: 16px;
    flex: none;
  }
</style>
</head>
<body>
<main class="canvas">
  <article class="business-card">
    <div class="card-frame"></div>

    <h1 class="brand-name">BRL Constructions</h1>

    <div class="person">
      <div class="person-name">John Smith</div>
      <div class="person-title">Project Manager</div>
    </div>

    <svg class="section-divider" width="40" height="110" viewBox="0 0 40 110" aria-hidden="true">
      <line x1="4" y1="2" x2="36" y2="108" stroke="var(--divider)" stroke-width="1.5"/>
    </svg>

    <ul class="contact-list">
      <li class="contact-item">
        <svg class="contact-icon" viewBox="0 0 16 16" aria-hidden="true">
          <path d="M4 1.5 L6 4.5 L4.8 6 C5.6 8 7.8 10.3 10 11.2 L11.5 10 L14.5 12 L13 14.5 C7 14 2 9 1.5 3 Z" fill="var(--accent-red)"/>
        </svg>
        <span>012 345 6789</span>
      </li>
      <li class="contact-item">
        <svg class="contact-icon" viewBox="0 0 16 16" aria-hidden="true">
          <rect x="1" y="3" width="14" height="10" fill="var(--accent-red)"/>
          <path d="M1 3 L8 9 L15 3" fill="none" stroke="#fff" stroke-width="1.2"/>
        </svg>
        <span>info@yourwebsite.com</span>
      </li>
      <li class="contact-item">
        <svg class="contact-icon" viewBox="0 0 16 16" aria-hidden="true">
          <circle cx="8" cy="8" r="7" fill="var(--accent-red)"/>
          <ellipse cx="8" cy="8" rx="3" ry="7" fill="none" stroke="#fff" stroke-width="1"/>
          <line x1="1" y1="8" x2="15" y2="8" stroke="#fff" stroke-width="1"/>
        </svg>
        <span>www.yourwebsite.com</span>
      </li>
    </ul>
  </article>
</main>
</body>
</html>
```